Product Description Graphic

We are designing a new product and need a better graphic to describe it.

We are not worried about names of the modules yet but want to be descriptive of capabilities. Right now "Present & CMA" should really be "Presentations & CMA".

I overall like the shape of the triangle and the arrow for Contacts but this is a very unsophisticated graphic done by a non-designer. Also need to better show that each block of capabilites will also have paywall capabilities.

Target Market(s)

Real Estate Brokerage Firms and Real Estate Agents

Industry/Entity Type

Real Estate

Colors

Designer to choose colors to be used in the design.

Requirements
Must have
• Sophisticated design. Paywall description embedded.

```html
<!DOCTYPE html>
<html lang="en">
<head>
<meta charset="utf-8">
<title>Product Capabilities Wheel</title>
<link rel="stylesheet" href="https://fonts.googleapis.com/css2?family=Nunito+Sans:wght@700;800;900&display=swap">
<style>
  :root {
    --bg: #ffffff;
    --frame: #e3e3e3;
    --label: #5c2384;
    --ink: #111111;
    --hatch: #3a1640;
    --core: #9e00ae;
    --pres-outer: #e61cc8;
    --pres-inner: #c215da;
    --mobile-outer: #e28aa8;
    --mobile-inner: #b86cc5;
    --link-outer: #dc0590;
    --web-outer: #e04fa2;
    --web-inner: #b445c4;
    --email-outer: #cc1e5c;
    --email-inner: #82168f;
  }
  html, body { margin: 0; padding: 0; overflow: hidden; background: var(--bg); }
  .canvas { width: 1200px; height: 1200px; position: relative; overflow: hidden; background: var(--bg); }
  .wheel { position: absolute; left: 0; top: 0; }
  .frame { fill: var(--frame); }
  .gap { stroke: var(--frame); stroke-width: 23; stroke-linecap: butt; fill: none; }
  .hatch-line { stroke: var(--hatch); stroke-width: 1; opacity: .7; }
  .module-label {
    font-family: "Nunito Sans", sans-serif;
    font-weight: 800;
    font-size: 27px;
    fill: var(--label);
    letter-spacing: .5px;
  }
  .core-label {
    font-family: "Nunito Sans", sans-serif;
    font-weight: 800;
    font-size: 21px;
    fill: #ffffff;
  }
  .legend-text {
    font-family: "Nunito Sans", sans-serif;
    font-weight: 800;
    font-size: 15px;
    fill: var(--ink);
  }
  .legend-line { stroke: #8a8a8a; stroke-width: 1; }
</style>
</head>
<body>
<div class="canvas">
<svg class="wheel" width="1200" height="1200" viewBox="0 0 1200 1200" xmlns="http://www.w3.org/2000/svg">
  <defs>
    <pattern id="paywall-hatch" patternUnits="userSpaceOnUse" width="22" height="22">
      <path class="hatch-line" d="M-2,-2 L24,24 M-13,9 L2,24 M9,-13 L24,2"/>
    </pattern>
    <path id="arc-presentations" d="M600,298 A302 302 0 0 1 902,600"/>
    <path id="arc-email" d="M318.1,702.6 A300 300 0 0 1 497.4,318.1"/>
    <path id="arc-mobile" d="M759,875.4 A318 318 0 0 0 916.8,627.7"/>
    <path id="arc-websites" d="M317.7,763 A326 326 0 0 0 684.4,914.9"/>
  </defs>

  <circle class="frame" cx="600" cy="600" r="340"/>

  <!-- Outer paywall rings -->
  <g class="paywall-ring">
    <path fill="var(--pres-outer)" d="M600,600 L600,310 A290 290 0 0 1 890,600 Z"/>
    <path fill="var(--mobile-outer)" d="M600,600 L890,600 A290 290 0 0 1 699.2,872.6 Z"/>
    <path fill="var(--link-outer)" d="M600,600 L699.2,872.6 A290 290 0 0 1 600,890 Z"/>
    <path fill="var(--web-outer)" d="M600,600 L600,890 A290 290 0 0 1 391.5,801.5 Z"/>
    <path fill="var(--email-outer)" d="M600,600 L391.5,801.5 A290 290 0 0 1 600,310 Z"/>
    <circle cx="600" cy="600" r="290" fill="url(#paywall-hatch)"/>
  </g>

  <!-- Core capability blocks -->
  <g class="capability-blocks">
    <path fill="var(--pres-inner)" d="M600,600 L600,360 A240 240 0 0 1 840,600 Z"/>
    <path fill="var(--mobile-inner)" d="M600,600 L840,600 A240 240 0 0 1 682.1,825.6 Z"/>
    <path fill="var(--web-inner)" d="M600,600 L600,840 A240 240 0 0 1 427.4,766.8 Z"/>
    <path fill="var(--email-inner)" d="M600,600 L427.4,766.8 A240 240 0 0 1 600,360 Z"/>
  </g>

  <circle class="frame" cx="600" cy="600" r="148"/>

  <path class="contacts-link" fill="var(--core)" d="M600,600 L682.1,825.6 A240 240 0 0 1 600,840 Z"/>

  <g class="gaps">
    <line class="gap" x1="600" y1="600" x2="600" y2="300"/>
    <line class="gap" x1="600" y1="600" x2="900" y2="600"/>
    <line class="gap" x1="600" y1="600" x2="702.6" y2="881.9"/>
    <line class="gap" x1="600" y1="600" x2="600" y2="900"/>
    <line class="gap" x1="600" y1="600" x2="384.2" y2="808.4"/>
  </g>

  <circle class="contacts-core" cx="600" cy="600" r="121" fill="var(--core)"/>
  <text class="core-label" x="600" y="609" text-anchor="middle">CONTACTS</text>

  <text class="module-label"><textPath href="#arc-presentations" startOffset="50%" text-anchor="middle">Presentations</textPath></text>
  <text class="module-label"><textPath href="#arc-email" startOffset="50%" text-anchor="middle">Email Nateure Print</textPath></text>
  <text class="module-label"><textPath href="#arc-mobile" startOffset="50%" text-anchor="middle">Mobile</textPath></text>
  <text class="module-label"><textPath href="#arc-websites" startOffset="50%" text-anchor="middle">Websites &amp; Leads</textPath></text>

  <g class="legend">
    <line class="legend-line" x1="880" y1="970" x2="905" y2="995"/>
    <line class="legend-line" x1="905" y1="970" x2="930" y2="995"/>
    <line class="legend-line" x1="872" y1="992" x2="905" y2="1025"/>
    <line class="legend-line" x1="872" y1="1020" x2="877" y2="1025"/>
    <text class="legend-text" x="962" y="993">Paywall</text>
    <text class="legend-text" x="962" y="1025">Feature</text>
  </g>
</svg>
</div>
</body>
</html>
```